International Employee Benefits

Create website including logo for Halvorsen Global
Specialising in setting up and managing employee benefits for multi-national companies
Should be professional and simple to navigate
Updates

Company name is Halvorsen Global

Please ensure the following is adhered to :

Page size - 950 pixels wide

If you plan to use a texture or picture background please ensure these are tiled so that the left edge matches the right edge like wallpaper.

The home page should have the logo at the top left of the screen followed by tabs "About Us", "Resources" "Expertise" "References" "Contact Us"
Perhaps there can also be an image on the home page, something that signifies global success??

The wording on the home page should be:

 Halvorsen Global brings a results oriented approach partnering with clients in mapping out customized strategies that meet their international objectives that save time and money and leaves an established process in place.  The client is supported with a high touch, one point of contact, that bring solutions to complex problems

 

Target Market(s)

Companies - HR and Finance

Industry/Entity Type

Employee

Requirements
Must have
• Map of world or globe

```html
<!DOCTYPE html>
<html lang="en">
<head>
<meta charset="utf-8">
<title>Halvorsen Global – International Employee Benefits</title>
<link rel="stylesheet" href="https://fonts.googleapis.com/css2?family=Oswald:wght@400;500&family=Roboto+Condensed:wght@400&display=swap">
<style>
  :root {
    --blue: #0aa0e6;
    --blue-deep: #0993d8;
    --grey-text: #666666;
    --grey-head: #6e6e6e;
    --tab-grey: #b9b9b9;
    --page-bg: #f4f4f3;
    --rule-grey: #cfcfcf;
    --white: #ffffff;
    --footer-brand: #a9dcf6;
  }
  * { margin: 0; padding: 0; box-sizing: border-box; }
  html, body { width: 1200px; height: 1016px; overflow: hidden; }
  body {
    background: var(--page-bg);
    font-family: "Roboto Condensed", "Arial Narrow", sans-serif;
    color: var(--grey-text);
    position: relative;
  }
  .abs { position: absolute; }

  /* header */
  .utility-links { left: 899px; top: 7px; display: flex; font-size: 14px; color: #9a9a9a; }
  .utility-links span { padding: 0 11px; border-left: 1px solid #d0d0d0; line-height: 11px; }
  .utility-links span:first-child { border-left: none; padding-left: 0; }
  .brand { left: 154px; top: 44px; font-family: "Oswald", sans-serif; font-weight: 500; font-size: 30px; color: var(--blue); text-transform: uppercase; letter-spacing: -0.5px; display: flex; align-items: center; gap: 10px; white-space: nowrap; }
  .brand-mark { width: 20px; height: 20px; background: var(--blue); flex: none; }
  .main-nav { top: 56px; left: 0; height: 40px; }
  .tab { position: absolute; top: 0; height: 40px; background: var(--tab-grey); color: var(--white); font-family: "Oswald", sans-serif; font-size: 18px; text-transform: uppercase; display: flex; align-items: center; justify-content: center; border-radius: 4px 4px 0 0; letter-spacing: -0.3px; white-space: nowrap; }
  .tab.active { background: var(--blue); }
  .tab.active::after { content: ""; position: absolute; bottom: 0; left: 50%; margin-left: -6px; border: 6px solid transparent; border-bottom-color: var(--white); }
  .header-rule { left: 0; top: 96px; width: 1200px; height: 4px; background: var(--blue); }

  /* hero */
  .hero { left: 154px; top: 112px; width: 890px; height: 332px; overflow: hidden; border-radius: 3px; box-shadow: 0 10px 14px -8px rgba(0,0,0,0.25); }
  .hero-photo { position: absolute; inset: 0; background: linear-gradient(100deg, #f2f3f4 0%, #e9ebee 35%, #b7a48e 48%, #d8d0c8 62%, #8d8f98 78%, #e6dcd2 100%); }
  .hero-wedge { position: absolute; left: 0; bottom: 0; }
  .hero-card { position: absolute; left: 0; top: 74px; width: 373px; height: 171px; background: rgba(255,255,255,0.93); border-radius: 0 4px 4px 0; padding: 14px 0 0 29px; font-family: "Oswald", sans-serif; text-transform: uppercase; white-space: nowrap; }
  .hero-card .lead { font-size: 30px; color: var(--grey-head); line-height: 34px; letter-spacing: -0.5px; }
  .hero-card .big { font-size: 74px; color: var(--blue); line-height: 70px; font-weight: 500; letter-spacing: -1.5px; }
  .hero-card .tail { font-size: 38px; color: var(--grey-head); line-height: 44px; letter-spacing: -0.8px; }
  .slider-dots { position: absolute; left: 10px; bottom: 9px; display: flex; gap: 4px; }
  .slider-dots i { width: 13px; height: 13px; border-radius: 50%; border: 1.5px solid var(--white); display: block; }
  .slider-dots i.on { background: var(--white); }

  /* sections */
  .section-title { font-family: "Oswald", sans-serif; font-size: 25px; text-transform: uppercase; color: var(--grey-head); letter-spacing: -0.5px; line-height: 30px; }
  .section-title.blue { color: var(--blue); }
  .title-rule { height: 1px; background: var(--blue); }
  .title-rule::after { content: ""; position: absolute; right: 0; top: -2px; width: 5px; height: 5px; background: var(--blue); }
  .body-copy { font-size: 13px; line-height: 15.5px; color: var(--grey-text); }
  .soft-rule { height: 1px; background: var(--rule-grey); }
  .world-map { left: 202px; top: 630px; width: 403px; height: 176px; background: radial-gradient(ellipse at 50% 50%, #b5b5b5 0%, #c9c9c9 45%, rgba(244,244,243,0) 72%); }
  .column-divider { left: 653px; top: 532px; width: 1px; height: 267px; background: var(--rule-grey); }
  .portrait { width: 107px; height: 114px; background: linear-gradient(160deg, #e8e8e8, #a9a9a9 60%, #d6d6d6); border: 1px solid #e2e2e2; }
  .benefit-text { width: 252px; }
  .benefit-text p + p { margin-top: 8px; }
  .read-more { font-family: "Oswald", sans-serif; font-size: 13px; color: var(--blue); text-transform: uppercase; text-align: right; width: 200px; }

  /* footer */
  .site-footer { left: 154px; top: 833px; width: 889px; height: 173px; background: var(--blue-deep); border-radius: 3px; color: var(--white); }
  .footer-brand { position: absolute; left: 17px; top: 60px; font-family: "Oswald", sans-serif; font-weight: 500; font-size: 24px; color: var(--footer-brand); text-transform: uppercase; letter-spacing: -0.3px; display: flex; align-items: center; gap: 8px; white-space: nowrap; }
  .footer-brand .brand-mark { width: 16px; height: 16px; background: var(--footer-brand); }
  .footer-links { position: absolute; top: 24px; list-style: none; font-size: 14px; line-height: 22.7px; white-space: nowrap; }
  .copyright { position: absolute; left: 14px; top: 148px; font-size: 11.5px; }
  .social { position: absolute; top: 142px; display: flex; gap: 8px; left: 806px; }
  .social i { display: block; width: 14px; height: 14px; border-radius: 50%; background: var(--white); }
</style>
</head>
<body>

<header>
  <nav class="utility-links abs"><span>Home</span><span>Sitemap</span><span>Faq's</span></nav>
  <div class="brand abs"><span class="brand-mark"></span>Halvorsen Global</div>
  <nav class="main-nav abs">
    <span class="tab active" style="left:553px;width:91px">About Us</span>
    <span class="tab" style="left:645px;width:100px">Resources</span>
    <span class="tab" style="left:746px;width:91px">Expertise</span>
    <span class="tab" style="left:838px;width:109px">Refferences</span>
    <span class="tab" style="left:948px;width:96px">Contact Us</span>
  </nav>
  <div class="header-rule abs"></div>
</header>

<section class="hero abs">
  <div class="hero-photo" role="img" aria-label="Photo of smiling business colleagues working together at a laptop"></div>
  <svg class="hero-wedge" width="240" height="65" viewBox="0 0 240 65"><polygon points="0,0 240,65 0,65" fill="#0aa0e6"/></svg>
  <div class="hero-card">
    <div class="lead">You will have</div>
    <div class="big">Definitely</div>
    <div class="tail">A good start with us!</div>
  </div>
  <div class="slider-dots"><i class="on"></i><i></i><i></i><i></i></div>
</section>

<section class="who-we-are">
  <h2 class="section-title abs" style="left:154px;top:480px">Who we are</h2>
  <div class="title-rule abs" style="left:154px;top:517px;width:477px"></div>
  <p class="body-copy abs" style="left:154px;top:529px;width:480px">Halvorsen Global brings a results oriented approach partnering with clients in mapping out customized strategies that meet their international objectives that save time and money and leaves an established process in place.&nbsp; The client is supported with a high touch, one point of contact, that bring solutions to complex problems</p>
  <div class="soft-rule abs" style="left:284px;top:611px;width:231px"></div>
  <div class="world-map abs" role="img" aria-label="Grey map of the world"></div>
</section>

<div class="column-divider abs"></div>

<section class="employee-benefits">
  <h2 class="section-title blue abs" style="left:678px;top:480px">Employee Benefits</h2>
  <div class="title-rule abs" style="left:678px;top:517px;width:366px"></div>

  <div class="portrait abs" style="left:678px;top:532px" role="img" aria-label="Black and white portrait of a smiling senior employee"></div>
  <div class="benefit-text body-copy abs" style="left:792px;top:532px">
    <p>Praesent vestibulum aenean nonummy hendrerit mauris. Hasellus porta. Fusce suscipit varius mi cum sociis natoque penatibus et magnis dis parturient montes nascetur.</p>
    <p>Praesent vestibulum aenean nonummy hendrerit mauris.</p>
  </div>
  <div class="read-more abs" style="left:844px;top:632px">Read more</div>

  <div class="soft-rule abs" style="left:745px;top:662px;width:230px"></div>

  <div class="portrait abs" style="left:678px;top:675px" role="img" aria-label="Black and white portrait of a smiling young employee with glasses"></div>
  <div class="benefit-text body-copy abs" style="left:792px;top:674px">
    <p>Praesent vestibulum aenean nonummy hendrerit mauris. Hasellus porta. Fusce suscipit varius mi cum sociis natoque penatibus et magnis dis parturient montes nascetur.</p>
    <p>Praesent vestibulum aenean nonummy hendrerit mauris.</p>
  </div>
  <div class="read-more abs" style="left:844px;top:774px">Read more</div>
</section>

<footer class="site-footer abs">
  <div class="footer-brand"><span class="brand-mark"></span>Halvorsen Global</div>
  <ul class="footer-links" style="left:306px"><li>About Us</li><li>Testimonials</li><li>Our Staff</li><li>Events &amp; Press</li></ul>
  <ul class="footer-links" style="left:457px"><li>Contact Us</li><li>Solutions &amp; Training</li><li>Services</li><li>Production</li></ul>
  <ul class="footer-links" style="left:618px;top:23px"><li>Risk Management</li><li>Archives</li><li>Forums</li><li>Affiliate Program</li></ul>
  <ul class="footer-links" style="left:770px"><li>Strategies</li><li>FAQ</li><li>Solutions</li><li>Business Help</li></ul>
  <div class="copyright">© 2013, Halvorsen Global,All Rights Reserved.</div>
  <div class="social" aria-label="Social media links"><i></i><i></i></div>
</footer>

</body>
</html>
```